Voltline Assemblies, Inc. Business Card

Voltline has three operating entities and I'm looking for a standard business card template that can be used for Voltline and the three operating entities that the logo just get swapped out, but has a very similar look and feel. Ultimately if someone had a business card from each, they assume the organizations are related because they all have the same look and feel.
Below are our websites and I will attached the logos for each entity:
https://www.voltlineassemblies.example/
https://www.brantoceramic.example/
https://www.omra-kfsd.example/
https://www.summitbreaker.example/

Target Market(s)

US Voltline

Industry/Entity Type

US Voltline

Contact Information for Business Card

Normal stuff

```html
<!DOCTYPE html>
<html lang="en">
<head>
<meta charset="utf-8">
<title>Voltline Assemblies, Inc. Business Card</title>
<link rel="stylesheet" href="https://fonts.googleapis.com/css2?family=Lato:wght@400;700;900&display=swap">
<style>
  :root {
    --navy: #1f2d6b;
    --red: #c41e35;
    --ink: #4a4a4a;
    --card: #ffffff;
    --backdrop: #d9d9d9;
  }
  * { box-sizing: border-box; margin: 0; padding: 0; }
  html, body { width: 1200px; height: 800px; overflow: hidden; }
  body {
    background: var(--backdrop);
    font-family: "Lato", sans-serif;
    position: relative;
  }
  .card {
    position: absolute;
    width: 540px;
    height: 309px;
    background: var(--card);
    border-radius: 22px;
    box-shadow: 0 6px 18px rgba(0,0,0,0.18);
  }
  /* Contact side */
  .card--contact { left: 50px; top: 90px; }
  .brand-block {
    position: absolute;
    left: 48px; top: 62px;
    width: 190px;
    display: flex; flex-direction: column; align-items: center; gap: 16px;
  }
  .brand-dot {
    width: 120px; height: 120px; border-radius: 50%;
    background: var(--navy);
  }
  .brand-name {
    font-weight: 900; font-size: 26px; color: var(--navy);
    letter-spacing: 0.5px;
  }
  .contact-block {
    position: absolute; left: 272px; top: 64px;
  }
  .person-name {
    font-weight: 900; font-size: 22px; color: var(--navy);
    letter-spacing: 0.4px; text-transform: uppercase;
  }
  .person-title {
    font-size: 14px; color: var(--red); margin-top: 2px; margin-bottom: 16px;
  }
  .contact-list { list-style: none; }
  .contact-list li {
    display: flex; align-items: flex-start; gap: 8px;
    font-size: 13px; color: var(--ink); line-height: 19px;
  }
  .contact-list svg { flex: none; width: 12px; height: 12px; margin-top: 4px; fill: var(--red); }
  /* Brand side */
  .card--brand { left: 610px; top: 400px; }
  .brand-lockup {
    position: absolute; left: 0; right: 0; top: 96px;
    display: flex; align-items: center; justify-content: center; gap: 18px;
  }
  .brand-lockup .brand-dot { width: 84px; height: 84px; }
  .lockup-name {
    font-weight: 900; font-size: 34px; color: var(--navy); letter-spacing: 0.5px;
  }
  .web-address {
    position: absolute; left: 0; right: 0; bottom: 46px;
    text-align: center; font-size: 15px; color: var(--ink); letter-spacing: 1.5px;
  }
</style>
</head>
<body>

<section class="card card--contact">
  <div class="brand-block">
    <div class="brand-dot"></div>
    <div class="brand-name">Voltline</div>
  </div>
  <div class="contact-block">
    <div class="person-name">Daniel Harper</div>
    <div class="person-title">President</div>
    <ul class="contact-list">
      <li>
        <svg viewBox="0 0 12 12" aria-hidden="true"><path d="M6 0a4.2 4.2 0 0 0-4.2 4.2C1.8 7.4 6 12 6 12s4.2-4.6 4.2-7.8A4.2 4.2 0 0 0 6 0zm0 6a1.8 1.8 0 1 1 0-3.6A1.8 1.8 0 0 1 6 6z"/></svg>
        <span>4120 Birchwood Lane<br>Fairbrook, Alaska 34512</span>
      </li>
      <li>
        <svg viewBox="0 0 12 12" aria-hidden="true"><path d="M2.4 0.6l2 2-1 1.4c.7 1.6 2 2.9 3.6 3.6l1.4-1 2 2-1.2 2C4.8 10.4 1.6 7.2 0.4 1.8z"/></svg>
        <span>369-555-0142</span>
      </li>
      <li>
        <svg viewBox="0 0 12 12" aria-hidden="true"><path d="M3 0h6a1 1 0 0 1 1 1v10a1 1 0 0 1-1 1H3a1 1 0 0 1-1-1V1a1 1 0 0 1 1-1zm.4 1.4v8h5.2v-8z"/></svg>
        <span>369-555-0187</span>
      </li>
      <li>
        <svg viewBox="0 0 12 12" aria-hidden="true"><path d="M0 2h12v8H0zm1.2 1.2v.3L6 6.6l4.8-3.1v-.3z"/></svg>
        <span>info@voltlineassemblies.example</span>
      </li>
      <li>
        <svg viewBox="0 0 12 12" aria-hidden="true"><circle cx="6" cy="6" r="6"/><path d="M3 6h6M6 3v6" stroke="#fff" stroke-width="1"/></svg>
        <span>voltlineassemblies.example</span>
      </li>
    </ul>
  </div>
</section>

<section class="card card--brand">
  <div class="brand-lockup">
    <div class="brand-dot"></div>
    <div class="lockup-name">Voltline Assemblies, Inc.</div>
  </div>
  <div class="web-address">www.VoltlineAssemblies.example</div>
</section>

</body>
</html>
```